Retail soap display box and Label design template for premium handmade natural soap brand.

We need a retail display cardboard box and customisable label design for our premium natural soap. The same box will be used for all our soap types. The label will be different for each soap type and will need to be a template or customisable design (.psd preferred).

About us: "We create and make natural soap products from locally made and sourced ingredients such as Australian olive oil, Halvering Ridge honey and local goats milk. We hand make every bar. Cocoa and shea butters make our soap different from commercial brands, butters contain natural antioxidants and protecting, moisturising and emollient properties which improves skin condition. Or formula uses organic raw cocoa butter and shea butter, blended with olive, coconut and castor oils to produce a natural soap which leaves skin feeling nourished and soft, no dryness."

Our product retails for between AU$12 - AU$16 ea. You can view our social media here: Instagram: @brambleloftsoaps Web: brambleloftsoaps.com.au Currently we use a kraft label cigar band but you do not have to go with kraft.

The soap size is 90mm(L) x 60mm (H) x 30mm (D). The box design should communicate: 'natural' 'botanical' 'luxurious' 'individual' 'apothecary' 'organic' 'green beauty' 'premium'. The box design will be given to a packaging company to make.

I've included photos to give you an idea of our products and the logo for box placement.

The labels template should carry through the design theme and can wrap around the box (or be front and back). They have to have text spaces for the soap name, soap attributes (text), company information, ingredient list, barcode and weight.

Thank you!

Target Market(s)

Age group 30-65. Women who buy organic green beauty products, who prefer quality over cost, professionals, buy luxe brands. Men who purchase for women, men who buy quality over cost, men who spend on themselves.

Industry/Entity Type

Hair And Beauty

Requirements
Must have
• Look and feel that coveys 'natural' 'botanical' 'luxurious' 'individual' 'apothecary' 'organic' 'green beauty' 'premium'.
• Must be able to be given to to packaging manufacturer in correct file type to be made.
• Must have customisable template label (.psd). this should be able to be changed on a Mac and printed on a laser printer on gloss sticker paper.
Nice to have
• A small window in the box to view the soap. Any shape.
• Box should be one piece.

```html
<!DOCTYPE html>
<html lang="en">
<head>
<meta charset="utf-8">
<title>Bramble Loft Soap Co. – Soap Box Dieline</title>
<link href="https://fonts.googleapis.com/css2?family=Courier+Prime:wght@400;700&display=swap" rel="stylesheet">
<style>
  :root {
    --page: #ffffff;
    --board: #4a2816;
    --board-dark: #3a1f10;
    --cream: #f6ecdc;
    --cream-deep: #e6d4b8;
    --ink: #1e130c;
    --ink-soft: #3b2a1e;
    --border-dot: #8c7660;
    --ornament: #b89a7c;
    --art-light: #d9c3a6;
    --art-dark: #8a5a3a;
    --window: #ffffff;
  }
  * { box-sizing: border-box; margin: 0; padding: 0; }
  html, body { width: 1200px; height: 277px; overflow: hidden; background: var(--page); }
  body { font-family: "Courier Prime", "Courier New", monospace; color: var(--ink); }

  .dieline { position: relative; width: 1200px; height: 277px; }

  .glue-flap {
    position: absolute; left: 44px; top: 30px; width: 62px; height: 216px;
    background: var(--board-dark);
    clip-path: polygon(0 6%, 100% 0, 100% 100%, 0 94%);
  }
  .box-strip {
    position: absolute; left: 106px; top: 30px; width: 1050px; height: 216px;
    background: var(--board);
  }

  .panel {
    position: absolute; top: 34px; height: 208px;
    background: radial-gradient(ellipse at center, var(--cream) 40%, var(--cream-deep) 100%);
    text-align: center;
  }
  .panel::after {
    content: ""; position: absolute; inset: 5px;
    border: 2px dotted var(--border-dot); pointer-events: none;
  }
  .panel--back   { left: 112px;  width: 408px; }
  .panel--side-a { left: 526px;  width: 104px; }
  .panel--front  { left: 637px;  width: 406px; }
  .panel--side-b { left: 1049px; width: 104px; }

  .brand-name { font-weight: 700; color: var(--ink); white-space: nowrap; }

  .brand-name--back {
    position: absolute; top: 28px; left: 0; right: 0;
    font-size: 19px; line-height: 24px;
  }
  .window {
    position: absolute; left: 32px; top: 66px; width: 338px; height: 78px;
    background: var(--window); border: 4px solid var(--board); border-radius: 14px;
  }
  .ingredients {
    position: absolute; left: 18px; right: 18px; top: 154px;
    font-size: 7.4px; line-height: 1.4; color: var(--ink-soft);
  }
  .shop-band {
    position: absolute; left: 122px; top: 190px; width: 164px; height: 16px;
    background: var(--board); color: var(--cream);
    font-size: 7px; line-height: 16px; white-space: nowrap;
  }

  .brand-name--side {
    position: absolute; top: 32px; left: 0; right: 0;
    font-size: 11px; line-height: 1.35;
  }
  .made-in {
    position: absolute; top: 86px; left: 0; right: 0;
    font-size: 10px; line-height: 1.6; color: var(--ink);
  }
  .made-in .amp { font-weight: 700; }
  .website {
    position: absolute; bottom: 11px; left: 0; right: 0;
    font-size: 5.4px; font-weight: 700; color: var(--ink); white-space: nowrap;
  }

  .flourish {
    position: absolute; left: 14px; right: 14px; height: 24px;
    background: linear-gradient(90deg, transparent, var(--ornament) 15%, var(--ornament) 85%, transparent);
    opacity: .55; border-radius: 12px;
  }
  .flourish--top { top: 12px; }
  .flourish--bottom { bottom: 10px; }

  .front-art {
    position: absolute; left: 138px; top: 40px; width: 130px; height: 50px;
    border-radius: 50% 50% 12px 12px;
    background: radial-gradient(ellipse at center, var(--art-dark) 0%, var(--art-light) 80%);
    opacity: .8;
  }
  .front-mark {
    position: absolute; top: 98px; left: 0; right: 0;
    display: flex; align-items: center; justify-content: center; gap: 8px;
  }
  .front-mark .dot { width: 12px; height: 12px; border-radius: 50%; background: var(--board); }
  .front-mark .brand-name { font-size: 18px; line-height: 24px; }

  .soap-name {
    position: absolute; left: 111px; width: 184px; top: 145px; height: 22px;
    border-top: 2px solid var(--board); border-bottom: 2px solid var(--board);
    font-size: 13px; line-height: 18px; color: var(--ink); white-space: nowrap;
  }
</style>
</head>
<body>
<main class="dieline">
  <div class="glue-flap"></div>
  <div class="box-strip"></div>

  <section class="panel panel--back">
    <div class="brand-name brand-name--back">Bramble Loft Soap Co.</div>
    <div class="window" aria-label="Window to view the soap"></div>
    <p class="ingredients">Ingredients : Olive oil. Water. Coconut oil. Cocoa &amp; Shea Butters.<br>Castor oil. Essential oils of Lavender, Myrrh, Frankincense, Rose Geranium<br>Tea Tree &amp; Patchouli. Activated Charcoal. Kaolin Clay.</p>
    <div class="shop-band">Shop : www.brambleloftsoaps.com.au</div>
  </section>

  <section class="panel panel--side-a">
    <div class="brand-name brand-name--side">Bramble Loft<br>Soap Co.</div>
    <p class="made-in">Made<br><span class="amp">&amp;</span><br>Handcrafted<br>In<br>Australia</p>
    <div class="website">www.brambleloftsoaps.com.au</div>
  </section>

  <section class="panel panel--front">
    <div class="flourish flourish--top" role="img" aria-label="Ornate scrolling flourish border"></div>
    <div class="front-art" role="img" aria-label="Illustration of coconut, cocoa pod and shea nut"></div>
    <div class="front-mark">
      <span class="dot"></span>
      <span class="brand-name">Bramble Loft Soap Co.</span>
    </div>
    <div class="soap-name">Activated Charcoal</div>
    <div class="flourish flourish--bottom" role="img" aria-label="Ornate scrolling flourish border"></div>
  </section>

  <section class="panel panel--side-b">
    <div class="brand-name brand-name--side">Bramble Loft<br>Soap Co.</div>
    <p class="made-in">Made<br><span class="amp">&amp;</span><br>Handcrafted<br>In<br>Australia</p>
    <div class="website">www.brambleloftsoaps.com.au</div>
  </section>
</main>
</body>
</html>
```